Tolvane - online store for farm produce

Online store selling fresh produce (vegetables, fruits, dairy products, meat, ...) from various farmers. Every farm has its own shopping window - order page - just like a really simple web store.

Please check the attached design brief and mock-ups for further details.

Target Market(s)

People looking for fresh vegetables, fruit, meat, ... delivered from farms

Industry/Entity Type

Farming

Coding

Coded - Design and coding required

Number of Pages Required

5+ page

Font styles to use
Sans Serif

Requirements
Must have
• Custom design. Good UX/UI design, very functional.
Responsive using bootstrap 12 point grid system

```html
<!DOCTYPE html>
<html lang="en">
<head>
<meta charset="utf-8">
<title>Tolvane – farm produce store</title>
<link rel="stylesheet" href="https://fonts.googleapis.com/css2?family=IBM+Plex+Sans:wght@400;500;600;700&display=swap">
<style>
:root{
  --green:#78a03c;
  --green-dark:#5f8a2a;
  --ink:#1f1f1f;
  --white:#ffffff;
  --featured:#343434;
  --cookie:#e9e5e2;
  --footer:#1b1b1b;
  --line:#3a3a3a;
  --muted:#cfcfcf;
  --fb:#3b5bb5;
  --gg:#e03a2f;
}
*{box-sizing:border-box;margin:0;padding:0}
html,body{width:852px;height:1200px;overflow:hidden;background:var(--white)}
body{font-family:"IBM Plex Sans",Arial,sans-serif;color:var(--ink);position:relative}
.page{position:absolute;width:752px;height:2212px;transform:scale(.5246);transform-origin:0 0;overflow:hidden;background:var(--white)}
.page--plain{left:26px;top:21px}
.page--login{left:433px;top:21px}
.section{position:absolute;left:0;width:752px}
.abs{position:absolute}
.btn{position:absolute;background:var(--green);color:var(--white);font-weight:600;font-size:8px;letter-spacing:.3px;display:flex;align-items:center;justify-content:center;text-transform:uppercase}
.heading{position:absolute;font-weight:700;font-size:13px;letter-spacing:.3px;text-transform:uppercase}
.rule{position:absolute;width:40px;height:2px;background:var(--green)}
.copy{position:absolute;font-size:8.4px;line-height:12px}

/* header */
.site-header{top:0;height:47px;background:var(--white)}
.brand{position:absolute;display:flex;align-items:center;gap:6px;font-weight:700;letter-spacing:.6px;text-transform:uppercase}
.brand__dot{border-radius:50%;background:var(--green)}
.site-header .brand{left:83px;top:10px;font-size:15px}
.site-header .brand__dot{width:24px;height:24px}
.nav{position:absolute;top:19px;font-size:7.6px;font-weight:500;text-transform:uppercase}
.nav--login{top:13px;left:594px;width:77px;height:21px;border:1.5px solid var(--green);color:var(--green);font-weight:600;display:flex;align-items:center;justify-content:center}

/* hero */
.hero{top:47px;height:365px;background:linear-gradient(100deg,#6d5a4b 0%,#a8876f 22%,#c24a4a 40%,#8a3a3a 52%,#5c4c44 70%,#3a3634 100%)}
.hero__shade{position:absolute;inset:0;background:linear-gradient(180deg,rgba(255,255,255,.05),rgba(40,70,30,.25))}
.hero__kicker{position:absolute;left:477px;top:28px;color:var(--white);font-weight:700;font-size:15px;letter-spacing:.3px}
.hero__title{position:absolute;left:475px;top:44px;color:var(--white);font-weight:700;font-size:38px}
.hero__more{left:481px;top:102px;width:68px;height:22px;border:1.5px solid var(--white)}
.arrow{position:absolute;top:171px;width:23px;height:23px;background:rgba(0,0,0,.65)}

/* about */
.about{top:412px;height:341px;background:linear-gradient(90deg,#ffffff 0%,#fbfaf8 40%,#e7a86a 60%,#f0a43c 78%,#c46a2e 100%)}
.about .heading{left:83px;top:48px}
.about .rule{left:83px;top:70px}
.about .copy{left:83px;top:98px;width:240px}
.about .btn{left:83px;top:267px;width:95px;height:23px}

/* farmers */
.farmers{top:753px;height:467px;background:linear-gradient(180deg,#4e9ad8 0%,#8cc3ea 35%,#d7e9f3 58%,#7ea65a 78%,#4d6f2e 100%)}
.farmers .heading{left:277px;top:27px;color:var(--white)}
.farmers .rule{left:277px;top:49px;background:var(--white)}
.perk{position:absolute;width:200px;display:flex;gap:12px}
.perk__icon{flex:none;width:42px;height:42px;border-radius:50%;background:var(--white);display:flex;align-items:center;justify-content:center}
.perk__icon span{width:20px;height:20px;border-radius:50%;background:var(--green)}
.perk p{font-size:7.4px;line-height:8.8px;color:var(--ink)}
.signup{position:absolute;left:278px;top:311px;width:248px;height:156px;background:rgba(45,45,40,.78)}
.field{position:absolute;left:20px;width:210px;height:23px;background:var(--white);font-size:6.5px;padding-left:10px;display:flex;align-items:center;text-transform:uppercase}
.signup .btn{left:20px;top:113px;width:210px;height:29px;font-size:11px}

/* customers */
.customers{top:1220px;height:408px;background:linear-gradient(90deg,#ffffff 0%,#ffffff 42%,#efe3d2 56%,#c98a5e 74%,#8a6b52 90%,#5a4a3c 100%)}
.customers .heading{left:83px;top:32px}
.customers .rule{left:83px;top:54px}
.gain{position:absolute;left:83px;width:250px;display:flex;gap:9px;align-items:flex-start}
.gain__icon{flex:none;width:33px;height:33px;border-radius:50%;border:1.5px solid var(--green);display:flex;align-items:center;justify-content:center}
.gain__icon span{width:13px;height:13px;border-radius:50%;background:var(--green)}
.gain p{font-size:7.4px;line-height:8.8px;padding-top:1px}
.customers .btn{left:86px;top:353px;width:95px;height:22px}

/* featured */
.featured{top:1628px;height:315px;background:var(--featured);color:var(--white)}
.featured .heading{left:0;width:752px;text-align:center;top:28px}
.featured .rule{left:344px;top:52px;width:64px;background:var(--white)}
.featured__media{position:absolute;left:90px;top:84px;width:324px;height:202px;background:var(--white);display:flex;align-items:center;justify-content:center}
.featured__media div{width:250px;height:130px;border-radius:40px;background:radial-gradient(circle at 35% 50%,#d9423a 0%,#e8842e 30%,#86b240 55%,#c96a3a 75%,rgba(255,255,255,0) 80%)}
.featured__title{position:absolute;left:441px;top:100px;font-weight:700;font-size:10px;line-height:14px;text-transform:uppercase}
.featured .copy{left:443px;top:142px;width:222px;font-size:8px;line-height:11px;color:#ececec}
.featured__order{position:absolute;left:447px;top:240px;width:83px;height:25px;border:2px solid var(--white);font-weight:600;font-size:10px;display:flex;align-items:center;justify-content:center}

/* cookies */
.cookies{top:1943px;height:44px;background:var(--cookie)}
.cookies__label{position:absolute;left:105px;top:18px;font-size:7px;font-weight:700}
.cookies__text{position:absolute;left:197px;top:13px;width:300px;font-size:6.6px;line-height:9px}
.cookies .btn{left:606px;top:13px;width:43px;height:18px;font-size:7px}

/* footer */
.footer{top:1987px;height:225px;background:var(--footer);color:var(--white)}
.footer .brand{left:83px;top:36px;font-size:15px}
.footer .brand__dot{width:40px;height:40px}
.footer__col{position:absolute;top:30px;font-size:7.4px}
.footer__col h4{font-size:8px;font-weight:700;margin-bottom:14px}
.footer__col li{list-style:none;line-height:13px}
.contact{display:flex;gap:9px;margin-bottom:14px;line-height:10px}
.contact svg{flex:none}
.footer__rule{position:absolute;left:83px;top:183px;width:587px;height:1px;background:var(--line)}
.footer__legal{position:absolute;left:0;width:752px;text-align:center;top:201px;font-size:6.5px;color:var(--muted)}

/* login overlay */
.dim{position:absolute;inset:0;background:rgba(0,0,0,.64)}
.login{position:absolute;left:238px;top:187px;width:278px;height:268px;background:var(--white)}
.login__badge{position:absolute;left:113px;top:-30px;width:52px;height:52px;border-radius:50%;background:var(--white);display:flex;align-items:center;justify-content:center}
.login__badge span{width:26px;height:26px;border-radius:50%;background:var(--green)}
.login__title{position:absolute;top:26px;left:0;width:278px;text-align:center;font-weight:700;font-size:12px}
.login__field{position:absolute;left:29px;width:222px;height:26px;border:1px solid #555;font-size:6.5px;font-weight:600;padding-left:9px;display:flex;align-items:center}
.login .btn{left:29px;top:130px;width:222px;height:28px;font-size:9.5px}
.login__or{position:absolute;top:184px;left:0;width:278px;text-align:center;font-weight:600;font-size:9px}
.social{position:absolute;top:220px;width:90px;height:21px;color:var(--white);font-size:6.5px;display:flex;align-items:center;gap:12px;padding-left:8px}
.social--a{left:43px;background:var(--fb)}
.social--b{left:142px;background:var(--gg)}
.social i{width:6px;height:6px;border-radius:50%;background:var(--white);display:block}
</style>
</head>
<body>

<!-- Home page -->
<div class="page page--plain">
  <header class="section site-header">
    <div class="brand"><span class="brand__dot"></span>Tolvane</div>
    <span class="nav" style="left:355px">Current offer</span>
    <span class="nav" style="left:441px">Farm directory</span>
    <span class="nav" style="left:533px">Settings</span>
    <span class="nav nav--login">Farmer login</span>
  </header>

  <section class="section hero" role="img" aria-label="Photo of a smiling shopper taking a red pepper from a vendor at a vegetable market stall">
    <div class="hero__shade"></div>
    <div class="hero__kicker">WELCOME TO</div>
    <div class="hero__title">Tolvane</div>
    <div class="btn hero__more">Read more</div>
    <div class="arrow" style="left:0"><svg width="23" height="23" viewBox="0 0 23 23"><path d="M13 8l-4 3.5 4 3.5" fill="none" stroke="#fff" stroke-width="1.4"/></svg></div>
    <div class="arrow" style="left:729px"><svg width="23" height="23" viewBox="0 0 23 23"><path d="M10 8l4 3.5-4 3.5" fill="none" stroke="#fff" stroke-width="1.4"/></svg></div>
  </section>

  <section class="section about" role="img" aria-label="Photo of two farmers in caps shaking hands in silhouette against a sunset over a field">
    <h2 class="heading">What is this about</h2>
    <div class="rule"></div>
    <p class="copy">Lorem ipsum dolor sit amet, consectetur adipiscing elit, sed do eiusmod tempor incididunt ut labore et dolore magna aliqua. Ut enim ad minim veniam, quis nostrud exercitation ullamco laboris nisi ut aliquip ex ea commodo consequat. Duis aute irure dolor in reprehenderit in voluptate velit esse cillum dolore eu fugiat nulla pariatur. Excepteur sint occaecat cupidatat non proident, sunt in culpa qui officia deserunt mollit anim id est laborum quis nostrud exercitation ullamco laboris nisi ut aliquip ex ea commodo consequat. Duis aute irure dolor in repre henderit in voluptate velit esse cillum dolore eu fugiat nulla pariatur</p>
    <div class="btn">Product search</div>
  </section>

  <section class="section farmers" role="img" aria-label="Photo of a farmer in a straw hat and plaid shirt standing in a green crop field under blue sky">
    <h2 class="heading">Benefits for farmers</h2>
    <div class="rule"></div>
    <div class="perk" style="left:272px;top:79px"><div class="perk__icon"><span></span></div><p>Lorem ipsum dolor sit amet, consectetur adipiscing elit, sed do eiusmod tempor incididunt ut labore et dolore magna aliqua. Ut enim ad minim veniam, consectetur adipiscing elit, sed do eiusmod</p></div>
    <div class="perk" style="left:487px;top:79px"><div class="perk__icon"><span></span></div><p>Lorem ipsum dolor sit amet, consectetur adipiscing elit, sed do eiusmod tempor incididunt ut labore et dolore magna aliqua. Ut enim ad minim veniam, consectetur adipiscing elit, sed do eiusmod</p></div>
    <div class="perk" style="left:272px;top:155px"><div class="perk__icon"><span></span></div><p>Lorem ipsum dolor sit amet, consectetur adipiscing elit, sed do eiusmod tempor incididunt ut labore et dolore magna aliqua. Ut enim ad minim veniam, consectetur adipiscing elit, sed do eiusmod</p></div>
    <div class="perk" style="left:487px;top:155px"><div class="perk__icon"><span></span></div><p>Lorem ipsum dolor sit amet, consectetur adipiscing elit, sed do eiusmod tempor incididunt ut labore et dolore magna aliqua. Ut enim ad minim veniam, consectetur adipiscing elit, sed do eiusmod</p></div>
    <div class="perk" style="left:272px;top:232px"><div class="perk__icon"><span></span></div><p>Lorem ipsum dolor sit amet, consectetur adipiscing elit, sed do eiusmod tempor incididunt ut labore et dolore magna aliqua. Ut enim ad minim veniam, consectetur adipiscing elit, sed do eiusmod</p></div>
    <div class="perk" style="left:487px;top:232px"><div class="perk__icon"><span></span></div><p>Lorem ipsum dolor sit amet, consectetur adipiscing elit, sed do eiusmod tempor incididunt ut labore et dolore magna aliqua. Ut enim ad minim veniam, consectetur adipiscing elit, sed do eiusmod</p></div>
    <form class="signup">
      <div class="field" style="top:20px">Name</div>
      <div class="field" style="top:49px">Email</div>
      <div class="field" style="top:78px">Phone</div>
      <div class="btn">Submit</div>
    </form>
  </section>

  <section class="section customers" role="img" aria-label="Photo of a woman choosing carrots at a vegetable market stall">
    <h2 class="heading">Benefits for customers</h2>
    <div class="rule"></div>
    <div class="gain" style="top:76px"><div class="gain__icon"><span></span></div><p>Lorem ipsum dolor sit amet, consectetur adipiscing elit, sed do eiusmod tempor incididunt ut labore et dolore magna aliqua. Ut enim ad minim veniam, consectetur adipiscing elit, sed do eiusmod</p></div>
    <div class="gain" style="top:128px"><div class="gain__icon"><span></span></div><p>Lorem ipsum dolor sit amet, consectetur adipiscing elit, sed do eiusmod tempor incididunt ut labore et dolore magna aliqua. Ut enim ad minim veniam, consectetur adipiscing elit, sed do eiusmod</p></div>
    <div class="gain" style="top:182px"><div class="gain__icon"><svg width="15" height="13" viewBox="0 0 15 13"><rect x="1" y="8" width="2.5" height="5" fill="#78a03c"/><rect x="5" y="6" width="2.5" height="7" fill="#78a03c"/><rect x="9" y="3" width="2.5" height="10" fill="#78a03c"/><rect x="13" y="0" width="2" height="13" fill="#78a03c"/></svg></div><p>Lorem ipsum dolor sit amet, consectetur adipiscing elit, sed do eiusmod tempor incididunt ut labore et dolore magna aliqua. Ut enim ad minim veniam, consectetur adipiscing elit, sed do eiusmod</p></div>
    <div class="gain" style="top:237px"><div class="gain__icon"><span></span></div><p>Lorem ipsum dolor sit amet, consectetur adipiscing elit, sed do eiusmod tempor incididunt ut labore et dolore magna aliqua. Ut enim ad minim veniam, consectetur adipiscing elit, sed do eiusmod</p></div>
    <div class="gain" style="top:295px"><div class="gain__icon"><svg width="18" height="18" viewBox="0 0 18 18"><circle cx="9" cy="9" r="9" fill="#78a03c"/><path d="M5 9.3l2.7 2.7L13 6.5" fill="none" stroke="#fff" stroke-width="1.8"/></svg></div><p>Lorem ipsum dolor sit amet, consectetur adipiscing elit, sed do eiusmod tempor incididunt ut labore et dolore magna aliqua. Ut enim ad minim veniam, consectetur adipiscing elit, sed do eiusmod</p></div>
    <div class="btn">Product search</div>
  </section>

  <section class="section featured">
    <h2 class="heading">Featured product</h2>
    <div class="rule"></div>
    <div class="featured__media"><div role="img" aria-label="Photo of a wicker basket filled with peppers, tomatoes, grapes, oranges and carrots"></div></div>
    <h3 class="featured__title">Lorem ipsum dolor sit amet<br>consectetur adipiscing</h3>
    <p class="copy">Lorem ipsum dolor sit amet, consectetur adipiscing elit, sed do eiusmod tempor incididunt ut labore et dolore magna aliqua. Ut enim ad minim veniam, consectetur adipiscing elit, sed do eiusmod Nor again is there anyone who loves or pursues or desires to obtain pain of itself, because it is pain, but because occasionally circumstances</p>
    <div class="featured__order">ORDER NOW</div>
  </section>

  <section class="section cookies">
    <span class="cookies__label">WE USE COOKIES</span>
    <p class="cookies__text">On the other hand, we denounce with righteous indignation and dislike men who are so beguiled and demoralized by the charms of pleasure of the moment, so blinded</p>
    <div class="btn">Accept</div>
  </section>

  <footer class="section footer">
    <div class="brand"><span class="brand__dot"></span>Tolvane</div>
    <div class="footer__col" style="left:287px"><h4>MENU</h4><ul><li>CURRENT OFFER</li><li>FARM DIRECTORY</li><li>SETTINGS</li><li>TERMS</li></ul></div>
    <div class="footer__col" style="left:403px"><h4>CONTACT US</h4>
      <div class="contact"><svg width="14" height="14" viewBox="0 0 14 14"><circle cx="7" cy="7" r="7" fill="#fff"/><path d="M7 3.2a2.3 2.3 0 0 0-2.3 2.3C4.7 7.3 7 10.5 7 10.5s2.3-3.2 2.3-5A2.3 2.3 0 0 0 7 3.2z" fill="#1b1b1b"/></svg><span>Mill Yard, Hollow Lane, Brackton<br>Hollowshire, BK4 7QD</span></div>
      <div class="contact"><svg width="14" height="14" viewBox="0 0 14 14"><circle cx="7" cy="7" r="7" fill="#fff"/><path d="M4.5 4c.6-.6 1.2-.3 1.5.4l.4.9c.2.5-.3.9-.6 1.1.4.9 1 1.5 1.8 1.9.3-.3.7-.7 1.1-.5l.9.4c.7.3.9 1 .4 1.5-2.6 2-7.2-2.8-5.5-5.7z" fill="#1b1b1b"/></svg><span>Call Us<br>555.014.2200</span></div>
      <div class="contact"><svg width="14" height="14" viewBox="0 0 14 14"><circle cx="7" cy="7" r="7" fill="#fff"/><rect x="3.8" y="4.8" width="6.4" height="4.4" fill="#1b1b1b"/><path d="M3.8 4.8L7 7.3l3.2-2.5" fill="none" stroke="#fff" stroke-width=".7"/></svg><span>E mail Us<br>info@tolvane.com</span></div>
    </div>
    <div class="footer__col" style="left:601px"><h4>FOLLOW US</h4>
      <div class="contact"><svg width="14" height="14"><circle cx="7" cy="7" r="7" fill="#fff"/></svg><span>Like us on<br>FACELINK</span></div>
      <div class="contact"><svg width="14" height="14"><circle cx="7" cy="7" r="7" fill="#fff"/></svg><span>Follow us on<br>CHIRPER</span></div>
      <div class="contact"><svg width="14" height="14"><circle cx="7" cy="7" r="7" fill="#fff"/></svg><span>Follow us on<br>LINKWORK</span></div>
    </div>
    <div class="footer__rule"></div>
    <p class="footer__legal">Copyright © 2020 All Rights Reserved</p>
  </footer>
</div>

<!-- Home page with farmer login open -->
<div class="page page--login">
  <header class="section site-header">
    <div class="brand"><span class="brand__dot"></span>Tolvane</div>
    <span class="nav" style="left:355px">Current offer</span>
    <span class="nav" style="left:441px">Farm directory</span>
    <span class="nav" style="left:533px">Settings</span>
    <span class="nav nav--login">Farmer login</span>
  </header>
  <section class="section hero" role="img" aria-label="Photo of a smiling shopper taking a red pepper from a vendor at a vegetable market stall">
    <div class="hero__shade"></div>
    <div class="hero__kicker">WELCOME TO</div>
    <div class="hero__title">Tolvane</div>
    <div class="btn hero__more">Read more</div>
    <div class="arrow" style="left:0"></div>
    <div class="arrow" style="left:729px"></div>
  </section>
  <section class="section about" role="img" aria-label="Photo of two farmers shaking hands in silhouette at sunset">
    <h2 class="heading">What is this about</h2>
    <div class="rule"></div>
    <p class="copy">Lorem ipsum dolor sit amet, consectetur adipiscing elit, sed do eiusmod tempor incididunt ut labore et dolore magna aliqua. Ut enim ad minim veniam, quis nostrud exercitation ullamco laboris nisi ut aliquip ex ea commodo consequat. Duis aute irure dolor in reprehenderit in voluptate velit esse cillum dolore eu fugiat nulla pariatur. Excepteur sint occaecat cupidatat non proident, sunt in culpa qui officia deserunt mollit anim id est laborum quis nostrud exercitation ullamco laboris nisi ut aliquip ex ea commodo consequat. Duis aute irure dolor in repre henderit in voluptate velit esse cillum dolore eu fugiat nulla pariatur</p>
    <div class="btn">Product search</div>
  </section>
  <section class="section farmers" role="img" aria-label="Photo of a farmer in a straw hat standing in a crop field">
    <h2 class="heading">Benefits for farmers</h2>
    <div class="rule"></div>
    <div class="perk" style="left:272px;top:79px"><div class="perk__icon"><span></span></div><p>Lorem ipsum dolor sit amet, consectetur adipiscing elit, sed do eiusmod tempor incididunt ut labore et dolore magna aliqua. Ut enim ad minim veniam, consectetur adipiscing elit, sed do eiusmod</p></div>
    <div class="perk" style="left:487px;top:79px"><div class="perk__icon"><span></span></div><p>Lorem ipsum dolor sit amet, consectetur adipiscing elit, sed do eiusmod tempor incididunt ut labore et dolore magna aliqua. Ut enim ad minim veniam, consectetur adipiscing elit, sed do eiusmod</p></div>
    <div class="perk" style="left:272px;top:155px"><div class="perk__icon"><span></span></div><p>Lorem ipsum dolor sit amet, consectetur adipiscing elit, sed do eiusmod tempor incididunt ut labore et dolore magna aliqua. Ut enim ad minim veniam, consectetur adipiscing elit, sed do eiusmod</p></div>
    <div class="perk" style="left:487px;top:155px"><div class="perk__icon"><span></span></div><p>Lorem ipsum dolor sit amet, consectetur adipiscing elit, sed do eiusmod tempor incididunt ut labore et dolore magna aliqua. Ut enim ad minim veniam, consectetur adipiscing elit, sed do eiusmod</p></div>
    <div class="perk" style="left:272px;top:232px"><div class="perk__icon"><span></span></div><p>Lorem ipsum dolor sit amet, consectetur adipiscing elit, sed do eiusmod tempor incididunt ut labore et dolore magna aliqua. Ut enim ad minim veniam, consectetur adipiscing elit, sed do eiusmod</p></div>
    <div class="perk" style="left:487px;top:232px"><div class="perk__icon"><span></span></div><p>Lorem ipsum dolor sit amet, consectetur adipiscing elit, sed do eiusmod tempor incididunt ut labore et dolore magna aliqua. Ut enim ad minim veniam, consectetur adipiscing elit, sed do eiusmod</p></div>
    <form class="signup">
      <div class="field" style="top:20px">Name</div>
      <div class="field" style="top:49px">Email</div>
      <div class="field" style="top:78px">Phone</div>
      <div class="btn">Submit</div>
    </form>
  </section>
  <section class="section customers" role="img" aria-label="Photo of a woman choosing carrots at a market stall">
    <h2 class="heading">Benefits for customers</h2>
    <div class="rule"></div>
    <div class="gain" style="top:76px"><div class="gain__icon"><span></span></div><p>Lorem ipsum dolor sit amet, consectetur adipiscing elit, sed do eiusmod tempor incididunt ut labore et dolore magna aliqua. Ut enim ad minim veniam, consectetur adipiscing elit, sed do eiusmod</p></div>
    <div class="gain" style="top:128px"><div class="gain__icon"><span></span></div><p>Lorem ipsum dolor sit amet, consectetur adipiscing elit, sed do eiusmod tempor incididunt ut labore et dolore magna aliqua. Ut enim ad minim veniam, consectetur adipiscing elit, sed do eiusmod</p></div>
    <div class="gain" style="top:182px"><div class="gain__icon"><span></span></div><p>Lorem ipsum dolor sit amet, consectetur adipiscing elit, sed do eiusmod tempor incididunt ut labore et dolore magna aliqua. Ut enim ad minim veniam, consectetur adipiscing elit, sed do eiusmod</p></div>
    <div class="gain" style="top:237px"><div class="gain__icon"><span></span></div><p>Lorem ipsum dolor sit amet, consectetur adipiscing elit, sed do eiusmod tempor incididunt ut labore et dolore magna aliqua. Ut enim ad minim veniam, consectetur adipiscing elit, sed do eiusmod</p></div>
    <div class="gain" style="top:295px"><div class="gain__icon"><svg width="18" height="18" viewBox="0 0 18 18"><circle cx="9" cy="9" r="9" fill="#78a03c"/><path d="M5 9.3l2.7 2.7L13 6.5" fill="none" stroke="#fff" stroke-width="1.8"/></svg></div><p>Lorem ipsum dolor sit amet, consectetur adipiscing elit, sed do eiusmod tempor incididunt ut labore et dolore magna aliqua. Ut enim ad minim veniam, consectetur adipiscing elit, sed do eiusmod</p></div>
    <div class="btn">Product search</div>
  </section>
  <section class="section featured">
    <h2 class="heading">Featured product</h2>
    <div class="rule"></div>
    <div class="featured__media"><div role="img" aria-label="Photo of a basket of mixed fruit and vegetables"></div></div>
    <h3 class="featured__title">Lorem ipsum dolor sit amet<br>consectetur adipiscing</h3>
    <p class="copy">Lorem ipsum dolor sit amet, consectetur adipiscing elit, sed do eiusmod tempor incididunt ut labore et dolore magna aliqua. Ut enim ad minim veniam, consectetur adipiscing elit, sed do eiusmod Nor again is there anyone who loves or pursues or desires to obtain pain of itself, because it is pain, but because occasionally circumstances</p>
    <div class="featured__order">ORDER NOW</div>
  </section>
  <section class="section cookies">
    <span class="cookies__label">WE USE COOKIES</span>
    <p class="cookies__text">On the other hand, we denounce with righteous indignation and dislike men who are so beguiled and demoralized by the charms of pleasure of the moment, so blinded</p>
    <div class="btn">Accept</div>
  </section>
  <footer class="section footer">
    <div class="brand"><span class="brand__dot"></span>Tolvane</div>
    <div class="footer__col" style="left:287px"><h4>MENU</h4><ul><li>CURRENT OFFER</li><li>FARM DIRECTORY</li><li>SETTINGS</li><li>TERMS</li></ul></div>
    <div class="footer__col" style="left:403px"><h4>CONTACT US</h4>
      <div class="contact"><svg width="14" height="14"><circle cx="7" cy="7" r="7" fill="#fff"/></svg><span>Mill Yard, Hollow Lane, Brackton<br>Hollowshire, BK4 7QD</span></div>
      <div class="contact"><svg width="14" height="14"><circle cx="7" cy="7" r="7" fill="#fff"/></svg><span>Call Us<br>555.014.2200</span></div>
      <div class="contact"><svg width="14" height="14"><circle cx="7" cy="7" r="7" fill="#fff"/></svg><span>E mail Us<br>info@tolvane.com</span></div>
    </div>
    <div class="footer__col" style="left:601px"><h4>FOLLOW US</h4>
      <div class="contact"><svg width="14" height="14"><circle cx="7" cy="7" r="7" fill="#fff"/></svg><span>Like us on<br>FACELINK</span></div>
      <div class="contact"><svg width="14" height="14"><circle cx="7" cy="7" r="7" fill="#fff"/></svg><span>Follow us on<br>CHIRPER</span></div>
      <div class="contact"><svg width="14" height="14"><circle cx="7" cy="7" r="7" fill="#fff"/></svg><span>Follow us on<br>LINKWORK</span></div>
    </div>
    <div class="footer__rule"></div>
    <p class="footer__legal">Copyright © 2020 All Rights Reserved</p>
  </footer>

  <div class="dim"></div>
  <div class="login" role="dialog" aria-label="Farmer login">
    <div class="login__badge"><span></span></div>
    <h2 class="login__title">LOGIN</h2>
    <div class="login__field" style="top:58px">USERNAME</div>
    <div class="login__field" style="top:93px">PASSWORD</div>
    <div class="btn">Login</div>
    <div class="login__or">OR</div>
    <div class="social social--a"><i></i>Facelink login</div>
    <div class="social social--b"><i></i>Searchly &nbsp; login</div>
  </div>
</div>

</body>
</html>
```